Spirit Distillery needs website design for velmorastills.example

We are a spirit distillery located in Canberra, Australia. We are just about to begin production on our products: Gin, Coffee vodka, lemon myrtle vodka, and apple and cinnamon vodka.
Velmora is Ancient Greek Mythology meaning "elixir of the Gods" so Greek mythology incorporated in the website, as well as simple and user friendly layout and functionality would be great.
Pages would include:
Welcome page with links to:
Our Products (Gin, Coffee vodka, lemon myrtle vodka, and apple and cinnamon vodka)
Events (what events the distillery is attending or holding at the distillery site)
Shop (for bottle sales)
Stockists (where the bottles are sold)
Cocktail recipe page

```html
<!DOCTYPE html>
<html lang="en">
<head>
<meta charset="utf-8">
<title>Velmora Distillery</title>
<link rel="stylesheet" href="https://fonts.googleapis.com/css2?family=Oswald:wght@400;500;600&family=Lora:wght@400&family=Poppins:wght@400;500&display=swap">
<style>
:root{
  --gold:#c89b52;
  --gold-light:#e0b877;
  --ink:#111;
  --night:#14130d;
  --black:#000;
  --paper:#fff;
  --muted:#666;
  --line:#d9c9ad;
}
*{box-sizing:border-box;margin:0;padding:0}
html,body{width:1200px;height:3523px;overflow:hidden;background:var(--paper)}
body{position:relative;font-family:'Poppins',sans-serif;color:var(--ink)}
h1,h2,h3,h4,h5{font-weight:400}
.abs{position:absolute}
.head-band{left:0;top:0;width:1200px;height:538px;background:var(--night)}
.topbar{left:702px;top:0;height:30px;display:flex;align-items:center;gap:24px;font-family:'Oswald',sans-serif;font-size:11px;color:#fff;white-space:nowrap}
.topbar b{color:var(--gold);font-weight:400}
.shipping{left:970px;top:0;width:230px;height:30px;background:#e8dcc6;clip-path:polygon(24px 0,100% 0,100% 100%,0 100%);font-family:'Oswald',sans-serif;font-size:13px;color:#111;display:flex;align-items:center;justify-content:flex-end;padding-right:63px}
.brand{left:62px;top:22px;font-family:'Oswald',sans-serif;font-weight:500;font-size:40px;line-height:50px;letter-spacing:3px;color:var(--gold)}
.nav{left:457px;top:55px;display:flex;gap:31px;font-family:'Oswald',sans-serif;font-size:11px;line-height:14px;color:#fff;white-space:nowrap}
.nav .on{color:var(--gold)}
.cart{left:1006px;top:47px;width:131px;height:31px;background:var(--gold);color:#111;font-family:'Oswald',sans-serif;font-size:13px;display:flex;align-items:center;justify-content:center;gap:8px}
.hero{left:62px;top:94px;width:1075px;height:537px;border:2px solid var(--line);background:linear-gradient(90deg,#f3f3f5 0%,#eceef0 50%,#dfe5d6 72%,#c9d9a6 85%,#9fbf6a 100%)}
.hero-title{left:210px;top:284px;font-family:'Oswald',sans-serif;font-weight:500;font-size:40px;line-height:52px;color:#111;white-space:nowrap}
.hero-sub{left:290px;top:335px;font-family:'Oswald',sans-serif;font-size:19px;line-height:24px;color:#111;white-space:nowrap}
.btn{display:flex;align-items:center;justify-content:center;border:1px solid var(--gold);color:var(--gold);font-family:'Oswald',sans-serif;font-size:12px;background:transparent;white-space:nowrap}
.btn.fill{background:var(--gold);color:#111}
.sec-title{left:0;width:1200px;text-align:center;font-family:'Oswald',sans-serif;font-weight:400;font-size:40px;line-height:52px;color:#111}
.sec-title span{color:var(--gold)}
.prod{width:195px;height:275px;background:linear-gradient(180deg,#f1f1f1,#c9c9c9)}
.prod .bottle{position:absolute;left:62px;top:18px;width:70px;height:205px;border-radius:18px 18px 8px 8px;background:linear-gradient(180deg,#ddd 0,#ddd 18%,#8b5a2b 30%,#6e431f 100%)}
.prod .bottle.clear{background:linear-gradient(180deg,#e8e8e8,#f6f6f6 40%,#b99668 100%)}
.prod .bottle.lemon{background:linear-gradient(180deg,#e8e8e8,#eee7b0 40%,#b99a5c 100%)}
.prod .tag{position:absolute;left:0;bottom:0;width:100%;height:30px;background:#111;color:var(--gold);font-family:'Oswald',sans-serif;font-weight:500;font-size:14px;display:flex;align-items:center;justify-content:center}
.prod .tag.on{background:var(--gold);color:#111}
.welcome{left:0;top:1093px;width:1200px;height:424px;background:radial-gradient(ellipse at 55% 50%,#3b3624,#16140c 75%)}
.welcome h2{position:absolute;left:0;width:1200px;top:84px;text-align:center;font-family:'Oswald',sans-serif;font-weight:500;font-size:38px;line-height:48px;color:var(--gold)}
.welcome h3{position:absolute;left:0;width:1200px;top:132px;text-align:center;font-family:'Oswald',sans-serif;font-weight:400;font-size:18px;line-height:24px;color:var(--gold)}
.welcome p{position:absolute;left:200px;width:800px;top:170px;text-align:center;font-family:'Lora',serif;font-size:11px;line-height:19px;color:#d9d6cc;padding:0 2px}
.feat{width:181px;height:326px;border:1px solid var(--line);background:#fff}
.feat .bottle{position:absolute;left:58px;top:22px;width:64px;height:190px;border-radius:16px 16px 8px 8px;background:linear-gradient(180deg,#e2e2e2 0,#e2e2e2 18%,#8b5a2b 30%,#6e431f 100%)}
.feat .bottle.clear{background:linear-gradient(180deg,#e8e8e8,#f6f6f6 40%,#b99668 100%)}
.feat .bottle.lemon{background:linear-gradient(180deg,#e8e8e8,#eee7b0 40%,#b99a5c 100%)}
.feat .name{position:absolute;top:242px;width:100%;text-align:center;font-family:'Oswald',sans-serif;font-weight:500;font-size:12px;line-height:16px;color:#111}
.feat .fact{position:absolute;top:258px;width:100%;text-align:center;font-family:'Oswald',sans-serif;font-size:10px;line-height:14px;color:#666}
.feat .price{position:absolute;top:282px;width:100%;text-align:center;font-family:'Oswald',sans-serif;font-weight:500;font-size:15px;line-height:20px;color:var(--gold)}
.feat .btn{position:absolute;left:45px;top:312px;width:90px;height:30px;background:#fff}
.feat .btn.fill{background:var(--gold);color:#111}
.cocktail{left:0;top:2120px;width:1200px;height:425px;background:radial-gradient(ellipse at 35% 40%,#3a3626,#16140c 70%)}
.cocktail h2{position:absolute;left:200px;top:100px;font-family:'Oswald',sans-serif;font-weight:500;font-size:40px;line-height:50px;color:var(--gold);letter-spacing:1px}
.cocktail p{position:absolute;left:200px;top:168px;width:395px;font-family:'Lora',serif;font-size:11px;line-height:19px;color:#cfcabd}
.event-img{background:linear-gradient(135deg,#2f3a4a,#8a8f6a 60%,#c9c08a)}
.event h4{font-family:'Oswald',sans-serif;font-weight:500;font-size:12px;line-height:15px;color:#111}
.event p{font-size:10px;line-height:13px;color:#666;margin-top:14px}
.event .more{font-family:'Oswald',sans-serif;font-size:10px;color:var(--gold);margin-top:12px}
.footer{left:0;top:3170px;width:1200px;height:353px;background:var(--black);color:#fff}
.footer .flogo{position:absolute;left:200px;top:60px;font-family:'Oswald',sans-serif;font-weight:500;font-size:30px;line-height:38px;letter-spacing:2px;color:var(--gold)}
.footer .about{position:absolute;left:200px;top:116px;width:230px;font-size:9px;line-height:14px}
.footer .news{position:absolute;left:200px;top:168px;width:225px;height:31px;border:1px solid #fff;font-size:9px;display:flex;align-items:center;padding-left:12px}
.footer h5{position:absolute;font-family:'Oswald',sans-serif;font-weight:400;font-size:12px;color:var(--gold)}
.footer ul{position:absolute;list-style:none;font-size:9px;line-height:18.6px}
.contact-row{position:absolute;left:736px;font-size:10px;line-height:14px}
.contact-row b{display:block;color:var(--gold);font-weight:500}
.social{position:absolute;left:971px;width:28px;height:28px;border:1px solid var(--gold);border-radius:50%}
.social.on{background:var(--gold)}
.legal{position:absolute;top:292px;font-size:9px;white-space:nowrap}
</style>
</head>
<body>

<header>
  <div class="abs head-band"></div>
  <div class="abs topbar"><span><b>Email:</b> info@velmorastills.example</span><span><b>Call Us:</b> 123-456-0142</span></div>
  <div class="abs shipping">Free Shipping Over $100</div>
  <div class="abs brand">VELMORA</div>
  <nav class="abs nav"><span class="on">HOME</span><span>OUR PRODUCTS</span><span>EVENTS</span><span>SHOP</span><span>STOCKISTS</span><span>COCKTAIL RECIPE</span><span>CONTACT US</span></nav>
  <div class="abs cart"><svg width="14" height="12" viewBox="0 0 14 12"><path d="M0 1h2.5l2 7h7l1.5-5H4" fill="none" stroke="#111" stroke-width="1.2"/><circle cx="5.5" cy="10.5" r="1" fill="#111"/><circle cx="10.5" cy="10.5" r="1" fill="#111"/></svg>MY CART $0.00</div>
</header>

<section>
  <div class="abs hero" role="img" aria-label="Photo of a mint and lime cocktail with berries and a lemon half on a light table"></div>
  <h1 class="abs hero-title">WE ARE A SPIRIT DISTILLERY</h1>
  <p class="abs hero-sub">LOCATED IN CANBERRA, AUSTRALIA.</p>
  <div class="abs btn" style="left:363px;top:391px;width:131px;height:38px;background:rgba(255,255,255,.4)">SHOP NOW</div>
</section>

<section>
  <h2 class="abs sec-title" style="top:682px">OUR <span>PRODUCTS</span></h2>
  <div class="abs prod" style="left:62px;top:755px"><div class="bottle clear" role="img" aria-label="Gin bottle photo"></div><div class="tag">GIN VODKA</div></div>
  <div class="abs prod" style="left:282px;top:755px"><div class="bottle" role="img" aria-label="Coffee vodka bottle photo"></div><div class="tag">COFFEE VODKA</div></div>
  <div class="abs prod" style="left:502px;top:755px"><div class="bottle lemon" role="img" aria-label="Lemon myrtle vodka bottle photo"></div><div class="tag on">LEMON MYRTLE VODKA</div></div>
  <div class="abs prod" style="left:722px;top:755px"><div class="bottle" role="img" aria-label="Apple vodka bottle photo"></div><div class="tag">APPLE VODKA</div></div>
  <div class="abs prod" style="left:942px;top:755px"><div class="bottle" role="img" aria-label="Cinnamon vodka bottle photo"></div><div class="tag">CINNAMON VODKA</div></div>
</section>

<section class="abs welcome" role="img" aria-label="Dark background illustration of a Greek god">
  <h2>WELCOME TO VELMORA</h2>
  <h3>LOCATED IN CANBERRA, AUSTRALIA.</h3>
  <p>Lorem Ipsum is simply dummy text of the printing and typesetting industry. Lorem Ipsum has been the industry's standard<br>dummy text ever since the 1500s, when an unknown printer took a galley of type and scrambled it to make a type specimen book. It has survived not<br>only five centuries, but also the leap into electronic typesetting, remaining essentially unchanged. It was popularised in the 1960s with the release of<br>Lettrix sheets containing Lorem Ipsum passages, and more recently with desktop publishing software like Pagewright Studio<br>including versions of Lorem Ipsum ...</p>
  <div class="abs btn" style="left:534px;top:293px;width:132px;height:38px">ABOUT US</div>
</section>

<section>
  <h2 class="abs sec-title" style="top:1570px">FEATURED <span>PRODUCTS</span></h2>
  <div class="abs feat" style="left:200px;top:1646px"><div class="bottle" role="img" aria-label="Coffee vodka bottle photo"></div><div class="name">COFFEE VODKA</div><div class="fact">IT IS A LONG ESTABLISHED FACT</div><div class="price">$ 80.00</div><div class="btn">SHOP NOW</div></div>
  <div class="abs feat" style="left:406px;top:1646px"><div class="bottle clear" role="img" aria-label="Gin bottle photo"></div><div class="name">GIN VODKA</div><div class="fact">IT IS A LONG ESTABLISHED FACT</div><div class="price">$ 90.00</div><div class="btn fill">SHOP NOW</div></div>
  <div class="abs feat" style="left:612px;top:1646px"><div class="bottle lemon" role="img" aria-label="Lemon myrtle vodka bottle photo"></div><div class="name">CLEMON MYRTLE</div><div class="fact">IT IS A LONG ESTABLISHED FACT</div><div class="price">$ 90.00</div><div class="btn">SHOP NOW</div></div>
  <div class="abs feat" style="left:818px;top:1646px"><div class="bottle" role="img" aria-label="Coffee vodka bottle photo"></div><div class="name">COFFEE VODKA</div><div class="fact">IT IS A LONG ESTABLISHED FACT</div><div class="price">$ 80.00</div><div class="btn">SHOP NOW</div></div>
  <div class="abs btn" style="left:522px;top:2020px;width:156px;height:37px">VIEW ALL PRODUCTS</div>
</section>

<section class="abs cocktail" role="img" aria-label="Dark background illustration of a Greek statue">
  <h2>COCKTAIL RECIPE</h2>
  <p>The industry's standard dummy text ever since the 1500s, when an unknown printer took a galley of type and scrambled it to make a type specimen book. It has survived not only five centuries, but also the leap into electronic typesetting, remaining essentially ...</p>
  <div class="abs btn" style="left:200px;top:262px;width:131px;height:37px">EXPLORE MORE</div>
  <div class="abs" style="left:818px;top:0;width:319px;height:425px;background:linear-gradient(160deg,#6f6a5a,#9aa5b5 55%,#5e6f8a)" role="img" aria-label="Illustration of a Greek goddess in armour"></div>
  <div class="abs" style="left:727px;top:62px;width:182px;height:300px;background:linear-gradient(180deg,#3a3a3a,#b83a3a 55%,#e0892a 75%,#8fae4a)" role="img" aria-label="Photo of three colourful cocktails on a bar"></div>
</section>

<section>
  <h2 class="abs sec-title" style="top:2597px">UPCOMING <span>EVENTS</span></h2>
  <div class="abs event" style="left:200px;top:2700px;width:182px">
    <div class="event-img" style="height:182px" role="img" aria-label="Photo of cocktail shaker, ice and limes"></div>
    <h4 style="margin-top:17px">CONTRARY TO POPULAR LOREM<br>BELIEF, LOREM IPSUM</h4>
    <p>There are many variations of passages of Lorem Ipsum available, but the majority have suffered alteration in some form</p>
    <div class="more">READ MORE</div>
  </div>
  <div class="abs event-img" style="left:432px;top:2668px;width:337px;height:300px;background:linear-gradient(135deg,#6a4a8a,#c07a4a 50%,#d8a060)" role="img" aria-label="Photo of friends enjoying drinks at a bar"></div>
  <div class="abs event" style="left:457px;top:2908px;width:287px;background:#fff;text-align:center;padding-top:22px">
    <h4>CONTRARY TO POPULAR LOREM<br>BELIEF, LOREM IPSUM</h4>
    <p style="padding:0 12px">There are many variations of passages of Lorem Ipsum available, but the majority have alteration in some...</p>
    <div class="more">READ MORE</div>
  </div>
  <div class="abs event" style="left:818px;top:2700px;width:182px">
    <div class="event-img" style="height:182px;background:linear-gradient(135deg,#3a5a8a,#c0c8d0 60%,#e8e0c8)" role="img" aria-label="Photo of spirit being poured into shot glasses"></div>
    <h4 style="margin-top:17px">CONTRARY TO POPULAR LOREM<br>BELIEF, LOREM IPSUM</h4>
    <p>There are many variations of passages of Lorem Ipsum available, but the majority have suffered alteration in some form</p>
    <div class="more">READ MORE</div>
  </div>
  <div class="abs btn" style="left:534px;top:3072px;width:132px;height:36px">VIEW ALL EVENTS</div>
</section>

<footer class="abs footer">
  <div class="flogo">VELMORA</div>
  <p class="about">Lorem Ipsum is simply dummy text of the printing and typesetting industry. lorem Ipsum</p>
  <div class="news">Enter your Name<svg style="position:absolute;right:10px" width="12" height="10" viewBox="0 0 12 10"><path d="M0 0l12 5-12 5 2-5z" fill="var(--gold)"/></svg></div>
  <h5 style="left:558px;top:62px">QUICK LINKS</h5>
  <ul style="left:560px;top:94px"><li>Home</li><li>Our Products</li><li>Events</li><li>Shop</li><li>Stockists</li><li>Cocktail Recipe</li><li>Contact Us</li></ul>
  <h5 style="left:736px;top:62px">CONTACT US</h5>
  <svg class="abs" style="left:736px;top:96px" width="18" height="18" viewBox="0 0 18 18"><path d="M4 2l3 3-2 2c1 2 3 4 5 5l2-2 3 3-2 3C7 16 2 11 1 4z" fill="none" stroke="var(--gold)" stroke-width="1.2"/></svg>
  <div class="contact-row" style="top:92px;left:766px"><b>Call</b>123-456-0142</div>
  <svg class="abs" style="left:738px;top:140px" width="16" height="20" viewBox="0 0 16 20"><path d="M8 19C3 12 1 9 1 7a7 7 0 0114 0c0 2-2 5-7 12z" fill="none" stroke="var(--gold)" stroke-width="1.2"/><circle cx="8" cy="7" r="2.5" fill="none" stroke="var(--gold)" stroke-width="1.2"/></svg>
  <div class="contact-row" style="top:136px;left:766px;width:170px"><b>Address</b>lorem ipsum work harbour ipsum - 12345</div>
  <svg class="abs" style="left:736px;top:200px" width="20" height="14" viewBox="0 0 20 14"><rect x="1" y="1" width="18" height="12" fill="none" stroke="var(--gold)" stroke-width="1.2"/><path d="M1 1l9 7 9-7" fill="none" stroke="var(--gold)" stroke-width="1.2"/></svg>
  <div class="contact-row" style="top:194px;left:766px"><b>Email</b>inf@velmorastills.example</div>
  <div class="social" style="top:67px"></div>
  <div class="social on" style="top:101px"></div>
  <div class="social" style="top:136px"></div>
  <div class="legal" style="left:200px">Copyright © 2021 <span style="color:var(--gold)">Velmora</span>. All Right Reserved</div>
  <div class="legal" style="left:560px;word-spacing:2px">Delivery &nbsp;&nbsp; / &nbsp;&nbsp; Terms &amp; Conditions &nbsp;&nbsp; / &nbsp;&nbsp; Privacy Policy</div>
</footer>

</body>
</html>
```